Emergency Dental Referral Company

I need a brochure to advertise my business to prospective dentists that may want to join or to dentists that may want to use this for their own patients. I also need to advertise this brochure to ER physicians who see many dental emergencies. This brochure is meant to be dual purpose: advertise our company and services to the ER physicians who then hand out the brochures to the dental emergency patients in pain. See our website for further details at www.molarquickfix.com

I will also be attaching our logo design.

Target Market(s)

Emergency Room physicians and other medical personnel who will distribute these brochures to patients in dental pain and dental emergencies

Industry/Entity Type

Business

Font styles to use
Serif
Sans Serif

Requirements
Must have
• Must be simple! Must have a call to action- inspiration to go to website. Highlight our guarantee that states "If you are not seen by a dentist in 24 hours or less, you will receive your money back. Emphasis on the logo. Must discuss how we find a dentist in your zip code in three easy steps.
• For the color- please make similar to our website of www.molarquickfix.com
Nice to have
• Would like to state that this service can see patients at any hour of the day.
Should not have
• no contact information besides the URL. www.molarquickfix.com

```html
<!DOCTYPE html>
<html lang="en">
<head>
<meta charset="utf-8">
<title>Molar Quick Fix – Find a Dentist in 3 Easy Steps</title>
<link rel="stylesheet" href="https://fonts.googleapis.com/css2?family=Oswald:wght@400;500;600&family=Open+Sans:wght@400;600;700;800&display=swap">
<style>
  :root {
    --brand-blue: #3d6db5;
    --brand-green: #8cc43f;
    --ink: #1d1d1d;
    --ink-soft: #3a3a3a;
    --paper: #f7f8f8;
    --paper-shade: #e6e9ea;
    --logo-grey: #555a5e;
    --white: #ffffff;
  }
  * { box-sizing: border-box; margin: 0; padding: 0; }
  html, body {
    width: 1200px;
    height: 800px;
    overflow: hidden;
    background: var(--paper);
  }
  .flyer {
    position: relative;
    width: 1200px;
    height: 800px;
    background: linear-gradient(90deg, var(--white) 0%, var(--paper) 45%, var(--paper-shade) 100%);
    font-family: "Open Sans", Arial, sans-serif;
    color: var(--ink);
    overflow: hidden;
  }
  .hero-photo {
    position: absolute;
    left: 430px;
    top: 40px;
    width: 700px;
    height: 680px;
    background: radial-gradient(ellipse at 45% 45%, #d9c3b2 0%, #c9b8ab 30%, #cfd5dc 62%, rgba(230,233,234,0) 80%);
  }
  .headline {
    position: absolute;
    left: 70px;
    top: 80px;
    font-family: "Oswald", "Arial Narrow", sans-serif;
    text-transform: uppercase;
    line-height: 1;
  }
  .headline__lead {
    display: block;
    color: var(--brand-blue);
    font-weight: 500;
    font-size: 32px;
  }
  .headline__main {
    display: block;
    color: var(--brand-green);
    font-weight: 500;
    font-size: 64px;
    margin-top: 8px;
  }
  .steps {
    position: absolute;
    left: 70px;
    top: 230px;
    width: 400px;
    height: 490px;
    list-style: none;
  }
  .steps__rail {
    position: absolute;
    left: 20px;
    top: 0;
    width: 2px;
    height: 100%;
    background: var(--ink-soft);
  }
  .step {
    position: absolute;
    left: 0;
    padding-left: 54px;
  }
  .step::before {
    content: "";
    position: absolute;
    left: 14px;
    top: 22px;
    width: 14px;
    height: 14px;
    border: 2px solid var(--ink-soft);
    border-radius: 50%;
    background: var(--white);
  }
  .step--one { top: 40px; }
  .step--two { top: 200px; left: 8px; }
  .step--three { top: 360px; left: 16px; }
  .step__number {
    font-weight: 800;
    font-size: 28px;
    text-transform: uppercase;
    line-height: 1.2;
  }
  .step__title {
    font-weight: 700;
    font-size: 19px;
    line-height: 1.3;
  }
  .step__text {
    font-size: 17px;
    line-height: 1.5;
    color: var(--ink-soft);
    max-width: 300px;
  }
  .brand {
    position: absolute;
    left: 820px;
    top: 100px;
    display: flex;
    align-items: center;
    gap: 16px;
  }
  .brand__mark {
    width: 40px;
    height: 40px;
    background: var(--brand-blue);
  }
  .brand__name {
    font-family: "Open Sans", Arial, sans-serif;
    font-weight: 700;
    font-size: 36px;
    color: var(--logo-grey);
    line-height: 1;
  }
  .guarantee-bar {
    position: absolute;
    left: 0;
    bottom: 0;
    width: 1200px;
    height: 88px;
    background: var(--brand-green);
    display: flex;
    align-items: center;
    justify-content: space-between;
    padding: 0 60px 0 70px;
    color: var(--white);
  }
  .guarantee {
    font-size: 20px;
    line-height: 1.25;
  }
  .guarantee strong { font-weight: 700; }
  .site-url {
    font-family: "Oswald", "Arial Narrow", sans-serif;
    font-weight: 600;
    font-size: 46px;
    text-transform: uppercase;
    letter-spacing: 0.5px;
  }
</style>
</head>
<body>
  <main class="flyer">
    <div class="hero-photo" role="img" aria-label="Photo of a smiling young woman with long brown hair, sitting with her arms folded over her knees"></div>

    <h1 class="headline">
      <span class="headline__lead">Find a dentist in</span>
      <span class="headline__main">3 easy steps</span>
    </h1>

    <ol class="steps">
      <li class="steps__rail" aria-hidden="true"></li>
      <li class="step step--one">
        <p class="step__number">Step 1</p>
        <p class="step__title">Fill out a Form</p>
        <p class="step__text">We will need your Zip code and contact information.</p>
      </li>
      <li class="step step--two">
        <p class="step__number">Step 2</p>
        <p class="step__title">Find a Dentist</p>
        <p class="step__text">Opportunity to choose among the most profitable and the most qualified dentist in your area.</p>
      </li>
      <li class="step step--three">
        <p class="step__number">Step 3</p>
        <p class="step__title">Get your appointment</p>
        <p class="step__text">Get your emergency appointment</p>
      </li>
    </ol>

    <div class="brand">
      <span class="brand__mark" aria-hidden="true"></span>
      <span class="brand__name">Molar Quick Fix</span>
    </div>

    <footer class="guarantee-bar">
      <p class="guarantee">If you are not seen by a dentist in 24 hours or less,<br><strong>you will receive your money back.</strong></p>
      <p class="site-url">www.molarquickfix.com</p>
    </footer>
  </main>
</body>
</html>
```